we are in the infrastructure business ( road construction ) and I need a billboard that I placed it at every project to illustrate that we worked there . We have the logo , I attached it , I just need an interesting design of the billboard.
The company s name is : Vextra Civil - I attached how to be written !
I don't need to write road construction business on it

Requirements
Must have
• Study the design of the logo I attached ( the sign with " KTP " is just an example !!
Nice to have
• the romanian flag but made into a special form ( I attached an Idea )

```html
<!DOCTYPE html>
<html lang="en">
<head>
<meta charset="utf-8">
<title>Vextra Civil – Project Billboard</title>
<link rel="stylesheet" href="https://fonts.googleapis.com/css2?family=Poppins:wght@400;600&display=swap">
<style>
  :root {
    --board-bg: #ffffff;
    --ink: #263845;
    --mark-cyan: #00c5f3;
    --flag-blue: #0f35c2;
    --flag-yellow: #dcb80e;
    --flag-red: #d0100f;
  }
  html, body {
    margin: 0;
    padding: 0;
    width: 1200px;
    height: 907px;
    overflow: hidden;
    background: var(--board-bg);
  }
  .billboard {
    position: relative;
    width: 1200px;
    height: 907px;
    background: var(--board-bg);
    font-family: "Poppins", sans-serif;
    color: var(--ink);
  }
  .flag-border {
    position: absolute;
    inset: 0;
    width: 1200px;
    height: 907px;
  }
  .brand-dot {
    position: absolute;
    left: 411px;
    top: 79px;
    width: 390px;
    height: 390px;
    border-radius: 50%;
    background: var(--mark-cyan);
  }
  .brand-name {
    position: absolute;
    margin: 0;
    font-weight: 600;
    line-height: 1;
    color: var(--ink);
  }
  .brand-name--primary {
    left: 180px;
    top: 528px;
    font-size: 150px;
    letter-spacing: 0.12em;
  }
  .brand-name--secondary {
    right: 124px;
    top: 652px;
    font-size: 96px;
    letter-spacing: 0.22em;
  }
  .website {
    position: absolute;
    left: 819px;
    top: 833px;
    margin: 0;
    font-size: 31px;
    font-weight: 400;
    color: var(--ink);
  }
</style>
</head>
<body>
  <main class="billboard">
    <svg class="flag-border" viewBox="0 0 1200 907" role="img" aria-label="Romanian flag colours in painted splash bands framing the top-right and bottom-left corners">
      <defs>
        <linearGradient id="fade-left" x1="1" y1="0" x2="0" y2="0">
          <stop offset="0" stop-color="var(--flag-blue)" stop-opacity="1"/>
          <stop offset="1" stop-color="var(--flag-blue)" stop-opacity="0"/>
        </linearGradient>
        <linearGradient id="fade-yellow-down" x1="0" y1="0" x2="0" y2="1">
          <stop offset="0.4" stop-color="var(--flag-yellow)" stop-opacity="1"/>
          <stop offset="1" stop-color="var(--flag-yellow)" stop-opacity="0"/>
        </linearGradient>
        <linearGradient id="fade-red-down" x1="0" y1="0" x2="0" y2="1">
          <stop offset="0.5" stop-color="var(--flag-red)" stop-opacity="1"/>
          <stop offset="1" stop-color="var(--flag-red)" stop-opacity="0"/>
        </linearGradient>
        <linearGradient id="fade-blue-up" x1="0" y1="1" x2="0" y2="0">
          <stop offset="0.5" stop-color="var(--flag-blue)" stop-opacity="1"/>
          <stop offset="1" stop-color="var(--flag-blue)" stop-opacity="0"/>
        </linearGradient>
        <linearGradient id="fade-yellow-up" x1="0" y1="1" x2="0" y2="0">
          <stop offset="0.4" stop-color="var(--flag-yellow)" stop-opacity="1"/>
          <stop offset="1" stop-color="var(--flag-yellow)" stop-opacity="0"/>
        </linearGradient>
        <linearGradient id="fade-right" x1="0" y1="0" x2="1" y2="0">
          <stop offset="0.3" stop-color="var(--flag-red)" stop-opacity="1"/>
          <stop offset="1" stop-color="var(--flag-red)" stop-opacity="0"/>
        </linearGradient>
      </defs>
      <g class="flag-corner flag-corner--top-right">
        <rect x="700" y="0" width="253" height="52" fill="url(#fade-left)"/>
        <rect x="953" y="0" width="169" height="225" fill="url(#fade-yellow-down)"/>
        <rect x="1122" y="0" width="78" height="500" fill="url(#fade-red-down)"/>
      </g>
      <g class="flag-corner flag-corner--bottom-left">
        <rect x="0" y="395" width="95" height="512" fill="url(#fade-blue-up)"/>
        <rect x="95" y="660" width="168" height="247" fill="url(#fade-yellow-up)"/>
        <rect x="263" y="838" width="410" height="69" fill="url(#fade-right)"/>
      </g>
    </svg>

    <div class="brand-dot" aria-hidden="true"></div>
    <h1 class="brand-name brand-name--primary">VEXTRA</h1>
    <p class="brand-name brand-name--secondary">CIVIL</p>

    <p class="website">www.vextracivil.com</p>
  </main>
</body>
</html>
```